Law Firm Corporate Identity Package

Stationery, fax, and business card.
Updates

Name of firm is "Halvorsen Law PC."

Target Market(s)

Real estate investor clients

Industry/Entity Type

Legal

Font styles to use
Serif

Colors
3277b5
85acd3

```html
<!DOCTYPE html>
<html lang="en">
<head>
<meta charset="utf-8">
<title>Halvorsen Law PC — Stationery</title>
<link rel="stylesheet" href="https://fonts.googleapis.com/css2?family=Arimo:wght@400;700&family=Didact+Gothic&display=swap">
<style>
  :root {
    --brand-blue: #3277b5;
    --brand-light: #85acd3;
    --brand-glow: #86addb;
    --paper: #ffffff;
    --ink: #3a3a3a;
    --backdrop: #e6e7e5;
  }
  * { box-sizing: border-box; margin: 0; padding: 0; }
  html, body { width: 1200px; height: 1039px; overflow: hidden; }
  body { background: var(--backdrop); position: relative; font-family: "Arimo", Arial, sans-serif; }

  .piece { position: absolute; background: var(--paper); overflow: hidden; }
  .piece svg.bands { position: absolute; left: 0; top: 0; }

  .brand-mark { position: absolute; background: var(--brand-blue); }
  .brand-name { position: absolute; color: var(--brand-blue); font-family: "Arimo", Arial, sans-serif; font-weight: 400; white-space: nowrap; }

  .address { position: absolute; font-family: "Didact Gothic", "Century Gothic", sans-serif; color: var(--ink); white-space: nowrap; }

  /* Letterhead */
  .letterhead { left: 48px; top: 133px; width: 553px; height: 781px; }
  .letterhead .brand-mark { left: 66px; top: 14px; width: 26px; height: 26px; }
  .letterhead .brand-name { left: 14px; top: 60px; font-size: 19px; }
  .letterhead .address { left: 13px; top: 716px; font-size: 8.5px; line-height: 10px; }

  /* Business card front */
  .card-front { left: 642px; top: 162px; width: 206px; height: 134px;
    background: radial-gradient(circle at 50% 45%, var(--brand-glow) 0%, var(--brand-blue) 75%); }
  .card-front .brand-name { color: var(--paper); left: 0; right: 0; top: 58px; text-align: center; font-size: 14px; }

  /* Business card back */
  .card-back { left: 864px; top: 162px; width: 206px; height: 134px; }
  .card-back .holder { position: absolute; right: 7px; top: 9px; text-align: right; color: var(--brand-blue); }
  .card-back .holder-name { font-weight: 700; font-size: 10px; line-height: 10px; }
  .card-back .holder-role { font-family: "Didact Gothic", sans-serif; font-size: 4px; letter-spacing: .2px; }
  .card-back .brand-mark { left: 44px; top: 11px; width: 15px; height: 15px; }
  .card-back .brand-name { left: 6px; top: 36px; font-size: 11px; }
  .card-back .address { left: 6px; top: 74px; font-size: 6px; line-height: 7.6px; }

  /* Envelope front */
  .envelope-front { left: 637px; top: 372px; width: 530px; height: 238px; }
  .envelope-front .brand-mark { left: 50px; top: 12px; width: 22px; height: 22px; }
  .envelope-front .brand-name { left: 6px; top: 47px; font-size: 16px; }
  .envelope-front .address { left: 11px; top: 160px; font-size: 8.5px; line-height: 10.8px; }

  /* Envelope back */
  .envelope-back { left: 637px; top: 674px; width: 530px; height: 238px; }
  .envelope-back .brand-name { color: var(--paper); left: 0; right: 0; top: 28px; text-align: center; font-size: 15px; }
</style>
</head>
<body>

<section class="piece letterhead" aria-label="Letterhead">
  <svg class="bands" width="553" height="781" viewBox="0 0 553 781">
    <polygon points="371,734 553,734 553,758 384,758" fill="var(--brand-light)"/>
    <polygon points="0,758 384,758 406,781 0,781" fill="var(--brand-blue)"/>
  </svg>
  <span class="brand-mark"></span>
  <span class="brand-name">Halvorsen Law PC</span>
  <p class="address">Halvorsen Law PC<br>Road, Area Name,<br>City, State. 00000<br>Phone: +1. 12345678</p>
</section>

<section class="piece card-front" aria-label="Business card front">
  <span class="brand-name">Halvorsen Law PC</span>
</section>

<section class="piece card-back" aria-label="Business card back">
  <svg class="bands" width="206" height="134" viewBox="0 0 206 134">
    <polygon points="122,112 206,112 206,123 131,123" fill="var(--brand-light)"/>
    <polygon points="0,123 131,123 138,134 0,134" fill="var(--brand-blue)"/>
  </svg>
  <div class="holder">
    <div class="holder-name">NAME HERE</div>
    <div class="holder-role">DESIGNATION</div>
  </div>
  <span class="brand-mark"></span>
  <span class="brand-name">Halvorsen Law PC</span>
  <p class="address">Halvorsen Law PC<br>Road, Area Name,<br>City, State. 00000<br>Phone: +1. 12345678<br>Fax: +1. 12345678</p>
</section>

<section class="piece envelope-front" aria-label="Envelope front">
  <svg class="bands" width="530" height="238" viewBox="0 0 530 238">
    <polygon points="370,196 530,196 530,218 386,218" fill="var(--brand-light)"/>
    <polygon points="0,218 386,218 400,238 0,238" fill="var(--brand-blue)"/>
  </svg>
  <span class="brand-mark"></span>
  <span class="brand-name">Halvorsen Law PC</span>
  <p class="address">Halvorsen Law PC<br>Road, Area Name,<br>City, State. 00000<br>Phone: +1. 12345678<br>Fax: +1. 12345678</p>
</section>

<section class="piece envelope-back" aria-label="Envelope back">
  <svg class="bands" width="530" height="238" viewBox="0 0 530 238">
    <defs>
      <radialGradient id="flap-glow" cx="50%" cy="40%" r="50%" gradientTransform="translate(0.25 0) scale(0.5 1)">
        <stop offset="0%" stop-color="var(--brand-glow)"/>
        <stop offset="100%" stop-color="var(--brand-blue)"/>
      </radialGradient>
    </defs>
    <path d="M0 0 H530 L515 58 Q511 74 495 74 H35 Q19 74 15 58 Z" fill="url(#flap-glow)"/>
  </svg>
  <span class="brand-name">Halvorsen Law PC</span>
</section>

</body>
</html>
```